new roofing company card

New primary business card for roofing company.

Industry/Entity Type

Residential roofing/Specializing in Asphalt and Standing seam metal roofing

Contact Information for Business Card

Phone number is: 555 471 2086 Email: support@halvenshingleworks.example website: www.halvenshingleworks.example

Colors
EB3D1F
EC4F4E
F09395
F8D3D4
FCEDEE

```html
<!DOCTYPE html>
<html lang="en">
<head>
<meta charset="utf-8">
<title>Halven Shingleworks — Business Card</title>
<link rel="stylesheet" href="https://fonts.googleapis.com/css2?family=Tinos:wght@400;700&display=swap">
<style>
  :root {
    --bg: #d4d4d4;
    --card: #ffffff;
    --red: #bf3028;
    --ink: #262826;
    --text: #2b2b2b;
  }
  * { box-sizing: border-box; margin: 0; padding: 0; }
  html, body { width: 1200px; height: 915px; overflow: hidden; }
  body {
    background: var(--bg);
    font-family: "Tinos", "Times New Roman", serif;
    color: var(--text);
    position: relative;
  }
  .card {
    position: absolute;
    width: 540px;
    height: 309px;
    background: var(--card);
    border-radius: 22px;
    overflow: hidden;
    box-shadow: 0 6px 18px rgba(0,0,0,0.22);
  }
  .card--front { left: 50px; top: 140px; }
  .card--back { left: 610px; top: 466px; }

  .wordmark {
    color: var(--ink);
    font-weight: 400;
    text-align: center;
    line-height: 1;
    letter-spacing: 1px;
    text-transform: uppercase;
    white-space: nowrap;
  }
  .card--front .wordmark {
    position: absolute;
    left: 0; right: 0; top: 52px;
    font-size: 40px;
  }
  .wordmark .mark-square {
    display: block;
    width: 22px; height: 22px;
    background: var(--red);
    margin: 0 auto 12px;
  }
  .wordmark span { display: block; }
  .wordmark span + span { margin-top: 6px; }

  .tagline-band {
    position: absolute;
    left: 0; right: 0; bottom: 0;
    height: 128px;
    background: var(--red);
    display: flex;
    align-items: center;
    justify-content: center;
    text-align: center;
    color: #fff;
    font-weight: 700;
    font-size: 23px;
    line-height: 1.25;
    padding: 0 30px;
  }

  .card--back .wordmark {
    position: absolute;
    left: 18px; top: 110px;
    width: 196px;
    font-size: 22px;
    letter-spacing: 0.5px;
  }
  .card--back .wordmark .mark-square {
    width: 18px; height: 18px;
    margin-bottom: 10px;
  }
  .divider {
    position: absolute;
    left: 228px; top: 70px;
    width: 2px; height: 120px;
    background: var(--red);
  }
  .contact {
    position: absolute;
    left: 246px; top: 64px;
    right: 16px;
  }
  .contact__name {
    color: var(--red);
    font-weight: 700;
    font-size: 24px;
    white-space: nowrap;
  }
  .contact__role {
    font-size: 15px;
    margin: 2px 0 12px 6px;
  }
  .contact__list { list-style: none; }
  .contact__list li {
    display: flex;
    align-items: center;
    gap: 9px;
    font-size: 14.5px;
    line-height: 1.5;
    white-space: nowrap;
  }
  .contact__list svg { width: 15px; height: 15px; flex: none; }

  .edge-strip { position: absolute; left: 0; bottom: 0; width: 540px; height: 16px; }
</style>
</head>
<body>

  <section class="card card--front" aria-label="Business card front">
    <div class="wordmark">
      <i class="mark-square"></i>
      <span>Halven</span>
      <span>Shingleworks</span>
    </div>
    <div class="tagline-band">
      Residential roofing/Specializing in Asphalt<br>and Standing seam metal roofing
    </div>
  </section>

  <section class="card card--back" aria-label="Business card back">
    <div class="wordmark">
      <i class="mark-square"></i>
      <span>Halven</span>
      <span>Shingleworks</span>
    </div>
    <div class="divider"></div>
    <div class="contact">
      <p class="contact__name">Marcus Delaney</p>
      <p class="contact__role">Owner</p>
      <ul class="contact__list">
        <li>
          <svg viewBox="0 0 16 16" aria-hidden="true"><circle cx="8" cy="8" r="8" fill="var(--red)"/><path d="M5 4.5l1.6-.4 1 2-1 .8a5 5 0 0 0 2.5 2.5l.8-1 2 1-.4 1.6c-3.6.2-6.7-2.9-6.5-6.5z" fill="#fff"/></svg>
          555 471 2086
        </li>
        <li>
          <svg viewBox="0 0 16 16" aria-hidden="true"><rect x="1" y="3.5" width="14" height="9" fill="var(--red)"/><path d="M1.5 4l6.5 5 6.5-5" fill="none" stroke="#fff" stroke-width="1.2"/></svg>
          support@halvenshingleworks.example
        </li>
        <li>
          <svg viewBox="0 0 16 16" aria-hidden="true"><circle cx="8" cy="8" r="8" fill="var(--red)"/><circle cx="8" cy="8" r="4.6" fill="none" stroke="#fff" stroke-width="1"/><path d="M3.4 8h9.2M8 3.4c-2 2.5-2 6.7 0 9.2M8 3.4c2 2.5 2 6.7 0 9.2" fill="none" stroke="#fff" stroke-width="0.9"/></svg>
          www.halvenshingleworks.example
        </li>
      </ul>
    </div>
    <svg class="edge-strip" viewBox="0 0 540 16" preserveAspectRatio="none" aria-hidden="true">
      <polygon points="0,4 330,4 318,16 0,16" fill="var(--ink)"/>
      <polygon points="338,0 540,0 540,16 324,16" fill="var(--red)"/>
    </svg>
  </section>

</body>
</html>
```